Commercial Construction Interior Fitout company needs Logo and Business Cards

We need a logo and business card design. We specialise in Commercial Ceilings, Partitions, Plastering and Carpentry.

Company name: 7QX Commercial Interiors. Would like a professional looking card more than a fancy look. Gloss front preferably black pattern with Fluro Green and white text.

Will need:

Name
Position
Phone
Fax
Email
Postal Address
Web address
Updates

Thank you so much everyone for your efforts and fantastic designs..   If I didn't respond to everyone personally,  my apologises. 

Again, thanks all

R.M                               

Target Market(s)

Existing & New clients in the Construction Industry

Industry/Entity Type

Business

Requirements
Nice to have
• 7QX to be overlapped or made into some sort of Logo

```html
<!DOCTYPE html>
<html lang="en">
<head>
<meta charset="utf-8">
<title>7QX Commercial Interiors – Logo &amp; Business Cards</title>
<link href="https://fonts.googleapis.com/css2?family=Open+Sans:wght@400;700;800&family=EB+Garamond:wght@400&family=Tinos&display=swap" rel="stylesheet">
<style>
  :root {
    --fluro-green: #6cbf3f;
    --faint-green: #e4efd9;
    --charcoal: #3b3b3b;
    --ink: #222222;
    --card-white: #ffffff;
    --card-black: #0c0c0c;
    --stage: #ebe7e0;
    --page: #ffffff;
  }
  * { margin: 0; padding: 0; box-sizing: border-box; }
  html, body { width: 1100px; height: 1200px; overflow: hidden; background: var(--page); }
  .canvas { position: relative; width: 1100px; height: 1200px; }

  .stage { position: absolute; left: 0; top: 0; width: 1100px; height: 872px; background: var(--stage); }

  /* Front (white) card */
  .card-front {
    position: absolute; left: 95px; top: 58px; width: 755px; height: 410px;
    background: var(--card-white); overflow: hidden;
    box-shadow: 0 3px 10px rgba(0,0,0,.18);
  }
  .wordmark {
    font-family: "Open Sans", sans-serif; font-weight: 800;
    color: var(--fluro-green); letter-spacing: -4px; line-height: 1;
  }
  .card-front .wordmark { position: absolute; left: 75px; top: 52px; font-size: 118px; }
  .card-front .tagline {
    position: absolute; left: 95px; top: 178px;
    font-family: "Open Sans", sans-serif; font-size: 25px; color: var(--ink);
  }
  .card-front .wordmark-faint {
    position: absolute; left: 420px; top: 160px; font-size: 170px;
    color: var(--faint-green); letter-spacing: -6px;
  }
  .name-plate {
    position: absolute; left: 422px; top: 62px; width: 238px; height: 42px;
    background: var(--card-black); text-align: center; padding-top: 2px;
  }
  .name-plate .person-name {
    font-family: "EB Garamond", serif; font-size: 21px; color: var(--fluro-green); line-height: 1.05;
  }
  .name-plate .person-role {
    font-family: "EB Garamond", serif; font-size: 12px; color: #ffffff; line-height: 1;
  }
  .contact-list {
    position: absolute; left: 112px; top: 240px; list-style: none;
    font-family: "Tinos", serif; font-size: 15px; color: var(--ink); line-height: 18px;
  }
  .contact-list li { display: flex; align-items: flex-start; gap: 8px; }
  .contact-list svg { flex: none; margin-top: 3px; }

  /* Back (black) card */
  .card-back {
    position: absolute; left: 200px; top: 424px; width: 735px; height: 410px;
    border-radius: 22px;
    background:
      repeating-linear-gradient(45deg, rgba(255,255,255,.035) 0 1px, transparent 1px 5px),
      repeating-linear-gradient(-45deg, rgba(0,0,0,.35) 0 1px, transparent 1px 5px),
      radial-gradient(ellipse at 50% 48%, #2e2e2e 0%, #161616 45%, var(--card-black) 100%);
    box-shadow: 0 6px 16px rgba(0,0,0,.35);
    text-align: center;
  }
  .card-back .wordmark { position: absolute; left: 0; right: 0; top: 100px; font-size: 150px; }
  .card-back .tagline {
    position: absolute; left: 0; right: 0; top: 262px;
    font-family: "Open Sans", sans-serif; font-size: 27px; color: #ffffff;
  }

  /* Flat logo variants */
  .logo-variant { position: absolute; top: 915px; width: 420px; text-align: center; }
  .logo-variant.primary { left: 115px; }
  .logo-variant.alternate { left: 620px; }
  .logo-variant .wordmark { font-size: 178px; }
  .logo-variant .tagline {
    margin-top: 14px;
    font-family: "Open Sans", sans-serif; font-size: 35px; color: #444444;
  }
</style>
</head>
<body>
<main class="canvas">
  <section class="stage">
    <article class="card-front">
      <div class="wordmark wordmark-faint">7QX</div>
      <div class="wordmark">7QX</div>
      <div class="tagline">Commercial Interiors</div>
      <div class="name-plate">
        <div class="person-name">Dana Kerr Whitfield</div>
        <div class="person-role">President</div>
      </div>
      <ul class="contact-list">
        <li>
          <svg width="13" height="13" viewBox="0 0 13 13" aria-hidden="true"><rect width="13" height="13" rx="2" fill="#222"/><path d="M3 8.5c0-2 1.5-3.5 3.5-3.5S10 6.5 10 8.5z" fill="#fff"/><rect x="3" y="3" width="7" height="1.6" fill="#fff"/></svg>
          <span>902.555.0148</span>
        </li>
        <li>
          <svg width="13" height="13" viewBox="0 0 13 13" aria-hidden="true"><rect width="13" height="13" rx="2" fill="#222"/><rect x="4" y="2.5" width="5" height="3" fill="#fff"/><rect x="2.5" y="6" width="8" height="4.5" fill="#fff"/></svg>
          <span>902.555.0193</span>
        </li>
        <li>
          <svg width="13" height="13" viewBox="0 0 13 13" aria-hidden="true"><rect width="13" height="13" rx="2" fill="#222"/><rect x="2.5" y="3.5" width="8" height="6" fill="#fff"/><path d="M2.5 3.5l4 3.5 4-3.5" stroke="#222" fill="none"/></svg>
          <span>hello@7qxinteriors.com.au</span>
        </li>
        <li>
          <svg width="13" height="13" viewBox="0 0 13 13" aria-hidden="true"><rect width="13" height="13" rx="2" fill="#222"/><circle cx="6.5" cy="6.5" r="4" fill="none" stroke="#fff"/><path d="M2.5 6.5h8M6.5 2.5v8" stroke="#fff"/></svg>
          <span>www.7qxinteriors.com.au</span>
        </li>
        <li>
          <svg width="13" height="13" viewBox="0 0 13 13" aria-hidden="true"><rect width="13" height="13" rx="2" fill="#222"/><path d="M6.5 11S3 7.5 3 5.3a3.5 3.5 0 0 1 7 0C10 7.5 6.5 11 6.5 11z" fill="#fff"/><circle cx="6.5" cy="5.3" r="1.3" fill="#222"/></svg>
          <span>1480 Harbour Line Rd<br>Westbury TN 38017</span>
        </li>
      </ul>
    </article>

    <article class="card-back">
      <div class="wordmark">7QX</div>
      <div class="tagline">Commercial Interiors</div>
    </article>
  </section>

  <section class="logo-variant primary">
    <div class="wordmark">7QX</div>
    <div class="tagline">Commercial Interiors</div>
  </section>
  <section class="logo-variant alternate">
    <div class="wordmark">7QX</div>
    <div class="tagline">Commercial Interiors</div>
  </section>
</main>
</body>
</html>
```